Business Card Design

we need a business card design and logo for a new cleaning company ,called brightwater cleaning Service,LLC .we provide cleaning services
Updates

i will also like to include the company's website in the business card   brightwatercleaningservice.example

Industry/Entity Type

Business

Contact Information for Business Card

Brightwater Cleaning Service,LLC
Marco Villanueva
Owner
marco@brightwatercleaningservice.example
Cell 555-318-7724
Office 555-374-6082

```html
<!DOCTYPE html>
<html lang="en">
<head>
<meta charset="utf-8">
<title>Brightwater Cleaning Service – Business Card</title>
<link rel="stylesheet" href="https://fonts.googleapis.com/css2?family=Open+Sans:wght@400;600;700;800&display=swap">
<style>
  :root {
    --green: #79b51c;
    --lime: #a9d13d;
    --white: #ffffff;
    --ink: #1c1c1c;
    --stage: #e9e9e6;
    --photo-tile: #d9cdb8;
    --photo-mop: #6f86b8;
    --photo-cloth: #e9b934;
  }
  * { box-sizing: border-box; margin: 0; padding: 0; }
  html, body {
    width: 1200px; height: 780px; overflow: hidden;
    background: var(--stage);
    font-family: "Open Sans", Arial, sans-serif;
  }
  .stage {
    width: 1200px; height: 780px;
    display: flex; flex-direction: column; align-items: center; justify-content: center;
    gap: 34px;
  }
  .card {
    position: relative;
    width: 640px; height: 340px;
    background: var(--white);
    overflow: hidden;
    box-shadow: 0 8px 24px rgba(0,0,0,0.18);
  }
  .card-header {
    position: absolute; left: 0; top: 0; width: 100%; height: 80px;
    background: var(--white);
    border-bottom: 4px solid var(--green);
    display: flex; align-items: center;
    padding-left: 30px;
    z-index: 2;
  }
  .company-name {
    color: var(--green);
    font-weight: 800;
    font-size: 29px;
    letter-spacing: 0.3px;
    text-transform: uppercase;
    white-space: nowrap;
  }
  .card-photo {
    position: absolute; left: 0; top: 84px; width: 100%; height: 190px;
  }
  .card-photo--mop {
    background: linear-gradient(120deg, var(--photo-tile) 0%, #e8dfcf 45%, var(--photo-mop) 80%, #3f5fa8 100%);
  }
  .card-photo--cloth {
    background: linear-gradient(120deg, var(--photo-cloth) 0%, #e8dfcf 35%, var(--photo-tile) 60%, #3f5fa8 100%);
  }
  .info-panel {
    position: absolute; left: 0; top: 150px; width: 590px; height: 124px;
    background: var(--white);
    border-top: 3px solid var(--green);
    display: flex; align-items: center;
    padding: 0 24px 0 30px;
    gap: 22px;
    z-index: 2;
  }
  .info-panel--front { width: 430px; }
  .info-notch {
    position: absolute; top: 147px; z-index: 3;
  }
  .person { flex: 0 0 170px; }
  .person--front { flex: 0 0 auto; }
  .person-name {
    color: var(--ink); font-weight: 800; font-size: 20px; line-height: 1.15;
    white-space: nowrap;
  }
  .person--front .person-name { font-size: 27px; }
  .person-title {
    color: var(--green); font-weight: 400; font-size: 16px;
    text-align: right; margin-top: 2px;
  }
  .person--front .person-title { font-size: 20px; }
  .contact-list { list-style: none; min-width: 0; }
  .contact-item {
    display: flex; align-items: center; gap: 9px;
    color: var(--ink); font-size: 14px; line-height: 1.6;
    white-space: nowrap;
  }
  .contact-bullet {
    width: 11px; height: 11px; background: var(--green); flex: none;
  }
  .card-footer {
    position: absolute; left: 0; bottom: 0; width: 100%; height: 66px;
    background: linear-gradient(180deg, var(--green) 0%, var(--lime) 100%);
    display: flex; align-items: center;
    padding-left: 30px;
  }
  .website {
    color: var(--white); font-size: 18px; font-weight: 400; letter-spacing: 1px;
  }
</style>
</head>
<body>
<main class="stage">
  <article class="card card--back">
    <header class="card-header">
      <h1 class="company-name">Brightwater Cleaning Service</h1>
    </header>
    <div class="card-photo card-photo--mop" role="img" aria-label="Photo of a yellow-handled mop with blue strands on a beige marble tile floor"></div>
    <section class="info-panel">
      <div class="person">
        <p class="person-name">Marco Villanueva</p>
        <p class="person-title">Owner</p>
      </div>
      <ul class="contact-list">
        <li class="contact-item"><span class="contact-bullet"></span>555-318-7724</li>
        <li class="contact-item"><span class="contact-bullet"></span>555-374-6082</li>
        <li class="contact-item"><span class="contact-bullet"></span>marco@brightwatercleaningservice.example</li>
      </ul>
    </section>
    <svg class="info-notch" style="left:200px" width="22" height="12" viewBox="0 0 22 12" aria-hidden="true">
      <polygon points="0,0 22,0 11,12" fill="var(--green)"/>
    </svg>
    <footer class="card-footer">
      <p class="website">www.brightwatercleaningservice.example</p>
    </footer>
  </article>

  <article class="card card--front">
    <header class="card-header">
      <h2 class="company-name">Brightwater Cleaning Service</h2>
    </header>
    <div class="card-photo card-photo--cloth" role="img" aria-label="Photo of a yellow cloth mop with a yellow handle on a marble tile floor"></div>
    <section class="info-panel info-panel--front">
      <div class="person person--front">
        <p class="person-name">Marco Villanueva</p>
        <p class="person-title">Owner</p>
      </div>
    </section>
    <svg class="info-notch" style="left:380px" width="22" height="12" viewBox="0 0 22 12" aria-hidden="true">
      <polygon points="0,0 22,0 11,12" fill="var(--green)"/>
    </svg>
    <footer class="card-footer">
      <p class="website">www.brightwatercleaningservice.example</p>
    </footer>
  </article>
</main>
</body>
</html>
```